4 Information One pagers needed for Australia's biggest Oil & Gas Conference

QOVRA is a global organisation with its corporate headquarters located in Perth, Western Australia and regional offices in Brisbane, Darwin, Singapore, Korea & China.
QOVRA delivers dedicated project support services, incorporating but not limited to; project design, procurement, construction, installation, commissioning, operations and maintenance. Our cross industry expertise, project expertise and track record of successfully delivering international projects with blue chip clients and partners has led to our fast evolving reputation as a preferred supplier worldwide within the oil and gas industry onshore and offshore within both greenfield and brownfield scopes.

Need to get information on a one page handout. There are 4 documents that need to be developed.

We need a banner across the top and bottom of each page, which has our logo, title of the document, and our contact details (Head Office – Address: Unit 14, 37-39 Harrow Lane, Perth WA 6000 Australia. Phone: +61 8 9471 5086) Needs to keep with the QOVRA colours but use images that are relevant to the oil and gas/commissioning industries. Our previous “who we are” flyer is attached so you have a feel for what we are after.

Page 1: QOVRA’ service offerings include (for each take brief paragraph from document attached for description of each. If unable to find information please contact us or search on www.fennmarsh-example.com):
• Engineering Design;
• Construction Management;
• Commissioning (Systems, Processes, Resources);
• Completions Strategy;
• Multi-Disciplinary Engineering;
• Multi-Disciplinary Technicians;
• Operations & Maintenance Support;
• EX Inspect & Maintain;
• On Site Nitrogen Production;
• Water Treatment;
• Compact Separation Systems;
• Processes to support services;
o Technology to improve efficiency and productivity (Finishline Bridge, QT Bridge).

Page 2: Our Team – please complete in order listed below and images are attached
Darren Kovalenko
Chief Executive Officer (CEO)
An extensively experienced and practical executive in the engineering industry with over 20 years’ service, more specifically in the oil and gas sector, since 1988.
The experience has been gained through a wide array of projects throughout Australia and Overseas working in the area of Design, System Analysing, Commissioning and Construction before commencing in Business Development and then finally Company Management and Directorships.
Darren has gained extensive experience in line and project management roles and more particularly in change management, people development and team motivation.
He has extensive experience leading and working in teams associated with design, construction and commissioning of world scale capital projects in both ‘brownfields’ and ‘Greenfields’ scenarios.
Keith Lambert
Chief Financial Officer
Keith is a qualified accountant (CGMA, CMA, CPA. MAAT) and brings to the team over 20 years of Australian and International experience in a number of key financial roles at both ASX listed and private companies. Keith comes to the team with a strong financial, commercial and business analytical skills combined with proven effective leadership of finance teams. Keith has significant experience in managing working capital requirements of growth businesses with an international footprint. Keith is a member of Australian Guild of Registered Ledger Advisers, Royal College of Cost Ledger Officers & Federation of Bookkeeping Practitioners.

Maree Tolvanen
HR Manager
Maree has more than 10 years’ experience across Oil & Gas, Resources, Engineering, and Finance industries. With general human resources experience, Maree has led strategic and operational HR support and services across recruitment, on boarding, training, remuneration and benefits, employment contract management, career planning and organisational accreditation for 457 visas. Further to this Maree has also managed HR within the M & A environment, through due diligence and post-acquisition integration on both buy and sell sides within the context of global organisations.

Gregory Nash
Project Services & Agency Representative
Project Services and Management expertise with local and international experience in the oil & gas, mining, and utilities industries, as well as a strong understanding within the finance sector. Gregory’s strengths and experience lie in developing and executing business proposals, as well as liaising with external consultants and clients. Possessing competent financial and economic modelling skills and the ability to utilise data for risk and profit based outcomes. Gregory has managed ISO 9001 implementation and ensures that all quality assurance processes are adhered to.
Gregory holds both Bachelor of Commerce and Master of Commerce (Economics & Finance) degrees and is working towards a Master of Science (Energy).

Trevor Dunstall
Director: QOVRA NT
Gregory has lived in the North of Australia for the last 26 years, bringing valuable local knowledge to the QOVRA NT office. He has owned and operated his NT services business for 17 years; servicing local and international clients before concentrating and moving into the Oil & Gas and Mining Sector. Gregory has many years of experience in logistics, service and supply, his extensive experience in the NT comes from the following industries: Oil & Gas; Mining; Exploration; Pastoral, Commercial Marine; and Construction.

Stuart Fenwick
Business Development Manager- Queensland
Stuart is a professional civil and mechanical engineer with more than 40 years’ experience in Australia and internationally, across consulting, construction and manufacturing sectors at operational and executive levels. He has held a number of senior executive roles with companies including Harlan Valve Systems, RTV Korvel, and Queensland Transit and has served on a number of industry associations, government committees and private sector boards.

Stuart has broad knowledge and experience in Australian and international business, with an extensive professional network throughout Australia, Asia, Europe and the United States. He has manufactured and supplied products to the oil and gas, petrochemical, power, water, military and nuclear industries.

Page 3: Our Influence
We need the headlines and logos of the following articles and publications:
https://www.tradewirewest.com.au/article/TVR-buys-Singapore-recruitment-firm?ref_K4pLmQ
http://www.fuelwirejournal-example.net/story.asp?id=413207591&section=careers
http://www.fuelwirejournal-example.net/story.asp?id=413207592&section=moves
Southern Crude & Pipeline Review – this one is getting published soon so just the logo for this one at this time?

Page 4: Who we work with?
Need to have just all logos of the companies that we have worked with. Attached is logos of our clients to match the list below. May need to find better resolution ones.
- Valtrop
- Kestrune Energy
- Norvane Global
- Brackmere
- MRP – Marlow Rigging Partners
- Tessaro
- Vantor Quell
- Hanul Coastal Fuel Company
- Corvo
- TL Group
- QN
- Lunden Rotors
- Orrin Petroleum
- Takka Energy
- Halberd Ridge Minerals (HRM)
- Wellspan Energy
- Tolsey Resources
- Glenrock Meats
- Drovan
- Pembury Ledger
- Varsell South Korea
- Clem Gully Iron Ore
- Westbrook Utility Holdings
- Falcrest Oil
- Solvant
- Tibbet Nickel
- Kvorn Oil
- Dravitel
- KMT
- Yarrandale Alumina

Industry/Entity Type

Oil And Gas

Font styles to use
Sans Serif
Other font styles liked:
• DIN Offc

Requirements
Must have
• 4 separate pages:
• 1. Menu of Services
• 2. Our Team
• 3. Our Influences (media companies)
• 4. Who we work with
• Keep in colours of QOVRA and ensure same header/footer used for all 4 pages
• orange = #D76927, R-215 G-105 B-39, CMYK C-11.65 M-70.4 Y-100 K-1.52
• Blue = #21224B, R-33 G-34 B-75, CMYK C-95.65, M-92.65 Y-39.82, K40.01
• Same theme across all 4
Nice to have
• Visually appealing
• Brief information
• Colour
• Images
Should not have
• Made up information - if unsure please contact us

```html
<!DOCTYPE html>
<html lang="en">
<head>
<meta charset="utf-8">
<title>QOVRA Team</title>
<link rel="stylesheet" href="https://fonts.googleapis.com/css2?family=Barlow:wght@300;400;500;600;700&display=swap">
<style>
:root{
  --orange:#D76927;
  --navy:#21224B;
  --text:#1d1e3a;
  --white:#ffffff;
}
*{margin:0;padding:0;box-sizing:border-box}
html,body{width:848px;height:1200px;overflow:hidden;background:var(--white)}
body{font-family:"Barlow",Arial,sans-serif;color:var(--text)}
.page{position:relative;width:848px;height:1200px;overflow:hidden;background:var(--white)}
.header-band{position:absolute;left:0;top:0;width:532px;height:152px;background:var(--orange)}
.page-title{position:absolute;left:38px;top:44px;font-size:58px;line-height:1;color:var(--white);letter-spacing:1px;white-space:nowrap}
.page-title .strong{font-weight:700}
.page-title .light{font-weight:300}
.brand{position:absolute;left:532px;top:0;width:316px;height:152px;display:flex;align-items:center;justify-content:center;gap:14px}
.brand-square{width:28px;height:28px;background:var(--orange)}
.brand-name{font-size:56px;font-weight:700;color:var(--navy);letter-spacing:3px;line-height:1}
.backdrop{position:absolute;left:0;top:152px;width:848px;height:896px;
  background:radial-gradient(ellipse at 75% 20%,#d9d9dc 0%,rgba(236,236,238,0) 55%),
             linear-gradient(180deg,#f2f2f3 0%,#e7e7ea 45%,#dcdce0 100%)}
.member{position:absolute;left:0;width:848px}
.portrait{position:absolute;left:46px;width:91px;height:122px;background:linear-gradient(160deg,#7fa9d4 0%,#4c6f96 60%,#2b2f45 100%)}
.bio{position:absolute;left:147px;width:657px}
.name{font-size:19.5px;font-weight:600;color:var(--navy);letter-spacing:.6px;line-height:1.1}
.role{font-size:13.6px;font-weight:600;color:var(--orange);letter-spacing:.4px;line-height:1.2;margin-top:1px}
.text{font-size:10.6px;line-height:13.6px;text-align:justify;margin-top:1px}
.footer{position:absolute;left:0;top:1048px;width:848px;height:152px;background:var(--navy)}
.footer-scene{position:absolute;inset:0;background:linear-gradient(90deg,#2a2b58 0%,#3a3b78 45%,#5a5c95 75%,#3a3b70 100%)}
.office{position:absolute;left:38px;top:36px;color:var(--white);font-size:15.6px;font-weight:600;line-height:20.4px;font-style:normal}
.web{position:absolute;left:624px;top:56px;width:224px;height:40px;background:var(--orange);color:var(--white);font-size:13px;font-weight:500;display:flex;align-items:center;justify-content:center;white-space:nowrap;letter-spacing:.3px}
</style>
</head>
<body>
<div class="page">
  <div class="header-band"></div>
  <h1 class="page-title"><span class="strong">QOVRA</span> <span class="light">TEAM</span></h1>
  <div class="brand"><span class="brand-square"></span><span class="brand-name">QOVRA</span></div>

  <div class="backdrop" role="img" aria-label="Faded greyscale photo of an oil and gas industrial site"></div>

  <section class="member" style="top:166px">
    <div class="portrait" style="top:22px" role="img" aria-label="Portrait photo of Darren Kovalenko"></div>
    <div class="bio">
      <h2 class="name">DARREN KOVALENKO</h2>
      <p class="role">CHIEF EXECUTIVE OFFICER (CEO)</p>
      <p class="text">An extensively experienced and practical executive in the engineering industry with over 20 years’ service, more specifically in the oil and gas sector, since 1988.<br>The experience has been gained through a wide array of projects throughout Australia and Overseas working in the area of Design, System Analysing, Commissioning and Construction before commencing in Business Development and then finally Company Management and Directorships.<br>Darren has gained extensive experience in line and project management roles and more particularly in change management, people development and team motivation.<br>He has extensive experience leading and working in teams associated with design, construction and commissioning of world scale capital projects in both ‘brownfields’ and ‘Greenfields’ scenarios.</p>
    </div>
  </section>

  <section class="member" style="top:345px">
    <div class="portrait" style="top:0" role="img" aria-label="Portrait photo of Keith Lambert"></div>
    <div class="bio">
      <h2 class="name">KEITH LAMBERT</h2>
      <p class="role">CHIEF FINANCIAL OFFICER</p>
      <p class="text">Keith is a qualified accountant (CGMA, CMA, CPA. MAAT) and brings to the team over 20 years of Australian and International experience in a number of key financial roles at both ASX listed and private companies. Keith comes to the team with a strong financial, commercial and business analytical skills combined with proven effective leadership of finance teams. Keith has significant experience in managing working capital requirements of growth businesses with an international footprint. Keith is a member of Australian Guild of Registered Ledger Advisers, Royal College of Cost Ledger Officers &amp; Federation of Bookkeeping Practitioners.</p>
    </div>
  </section>

  <section class="member" style="top:488px">
    <div class="portrait" style="top:-8px" role="img" aria-label="Portrait photo of Maree Tolvanen"></div>
    <div class="bio">
      <h2 class="name">MAREE TOLVANEN</h2>
      <p class="role">HR MANAGER</p>
      <p class="text">Maree has more than 10 years’ experience across Oil &amp; Gas, Resources, Engineering, and Finance industries. With general human resources experience, Maree has led strategic and operational HR support and services across recruitment, on boarding, training, remuneration and benefits, employment contract management, career planning and organisational accreditation for 457 visas. Further to this Maree has also managed HR within the M &amp; A environment, through due diligence and post-acquisition integration on both buy and sell sides within the context of global organisations.</p>
    </div>
  </section>

  <section class="member" style="top:614px">
    <div class="portrait" style="top:5px" role="img" aria-label="Portrait photo of Gregory Nash"></div>
    <div class="bio">
      <h2 class="name">GREGORY NASH</h2>
      <p class="role">PROJECT SERVICES &amp; AGENCY REPRESENTATIVE</p>
      <p class="text">Project Services and Management expertise with local and international experience in the oil &amp; gas, mining, and utilities industries, as well as a strong understanding within the finance sector. Gregory’s strengths and experience lie in developing and executing business proposals, as well as liaising with external consultants and clients. Possessing competent financial and economic modelling skills and the ability to utilise data for risk and profit based outcomes. Gregory has managed ISO 9001 implementation and ensures that all quality assurance processes are adhered to.<br>Gregory holds both Bachelor of Commerce and Master of Commerce (Economics &amp; Finance) degrees and is working towards a Master of Science (Energy).</p>
    </div>
  </section>

  <section class="member" style="top:774px">
    <div class="portrait" style="top:-10px" role="img" aria-label="Portrait photo of Trevor Dunstall"></div>
    <div class="bio">
      <h2 class="name">TREVOR DUNSTALL</h2>
      <p class="role">DIRECTOR: QOVRA NT</p>
      <p class="text">Gregory has lived in the North of Australia for the last 26 years, bringing valuable local knowledge to the QOVRA NT office. He has owned and operated his NT services business for 17 years; servicing local and international clients before concentrating and moving into the Oil &amp; Gas and Mining Sector. Gregory has many years of experience in logistics, service and supply, his extensive experience in the NT comes from the following industries: Oil &amp; Gas; Mining; Exploration; Pastoral, Commercial Marine; and Construction.</p>
    </div>
  </section>

  <section class="member" style="top:904px">
    <div class="portrait" style="top:6px" role="img" aria-label="Portrait photo of Stuart Fenwick"></div>
    <div class="bio">
      <h2 class="name">STUART FENWICK</h2>
      <p class="role">BUSINESS DEVELOPMENT MANAGER- QUEENSLAND</p>
      <p class="text">Stuart is a professional civil and mechanical engineer with more than 40 years’ experience in Australia and internationally, across consulting, construction and manufacturing sectors at operational and executive levels. He has held a number of senior executive roles with companies including Harlan Valve Systems, RTV Korvel, and Queensland Transit and has served on a number of industry associations, government committees and private sector boards.<br>Stuart has broad knowledge and experience in Australian and international business, with an extensive professional network throughout Australia, Asia, Europe and the United States. He has manufactured and supplied products to the oil and gas, petrochemical, power, water, military and nuclear industries.</p>
    </div>
  </section>

  <footer class="footer">
    <div class="footer-scene" role="img" aria-label="Navy-tinted photo of an offshore drilling rig and crane at dusk"></div>
    <address class="office">Head Office:<br>Unit 14, 37-39 Harrow Lane,<br>Perth WA 6000 Australia.<br>Phone: +61 8 9471 5086</address>
    <div class="web">WWW.FENNMARSH-EXAMPLE.COM</div>
  </footer>
</div>
</body>
</html>
```